Flyer Design Project

We are a storm restoration company that has recently begun restoration from water/flood damage from Hurricane Pellam. We provide disaster relief to homeowners and or commercial property owners after a flood. To start we offer cleanup and remediation which is taking out and disposing of all wet items in a home or business and the cutting out of walls, flooring and other items affected by a flood. We then provide remediation which includes the drying out of a home or business along with a dehumidifier to take all the moisture out of the air and to put it simply dry out the home. We also uses chemicals to clean and provide mold remediation to prevent to growth of mold. We work directly with a customers insurance company if they have flood insurance and after that we provide the services to rebuild and bring their property back to its condition before the storm.

Im looking for an informational type flier that I could insert into our business folders that we give to customers and also to use as fliers to pass out to potential customers. I want potential customers to look at this and feel comfortable with calling my company and working with us.

Company name Brindlewick Building Group. I attached our company logo.

Target Market(s)

Those affected by flooding from Hurricane Pellam

Industry/Entity Type

Insurance

Requirements
Must have
• Company logo, name and colors on flier
Nice to have
• Color photos that have to do with water restoration or showing flood damamge

```html
<!DOCTYPE html>
<html lang="en">
<head>
<meta charset="utf-8">
<title>Brindlewick Building Group – Water Restoration Flyer</title>
<link rel="stylesheet" href="https://fonts.googleapis.com/css2?family=Archivo:wght@600;700;800&display=swap">
<style>
  :root {
    --paper: #ffffff;
    --teal: #52c5cf;
    --navy: #1f2a4a;
    --white: #ffffff;
    --photo-dark: #2e2620;
    --photo-mid: #6d5a4b;
    --photo-brick: #8a4f3c;
    --photo-water: #9c8b78;
  }
  html, body {
    margin: 0;
    padding: 0;
    width: 939px;
    height: 1200px;
    overflow: hidden;
    background: var(--paper);
  }
  .flyer {
    position: relative;
    width: 939px;
    height: 1200px;
    background: var(--paper);
    font-family: "Archivo", "Arial Narrow", sans-serif;
    color: var(--white);
  }
  .hero {
    position: absolute;
    left: 26px;
    top: 0;
    width: 887px;
    height: 681px;
    background:
      linear-gradient(180deg, rgba(0,0,0,0.05) 0%, rgba(0,0,0,0.15) 55%, rgba(0,0,0,0.25) 100%),
      linear-gradient(90deg, var(--photo-brick) 0%, var(--photo-dark) 14%, var(--photo-mid) 30%, #5a4030 55%, var(--photo-dark) 70%, var(--photo-brick) 85%, #7a5a4a 100%);
  }
  .hero-water {
    position: absolute;
    left: 0;
    right: 0;
    bottom: 0;
    height: 290px;
    background: linear-gradient(180deg, rgba(156,139,120,0.55) 0%, rgba(120,100,82,0.85) 100%);
  }
  .service-callout {
    position: absolute;
    right: 76px;
    top: 150px;
    text-align: right;
    text-transform: uppercase;
    font-weight: 800;
    line-height: 1;
  }
  .service-callout .hours { font-size: 40px; }
  .service-callout .label { font-size: 28px; margin-top: 4px; }
  .service-callout .call { font-size: 28px; margin-top: 38px; }
  .service-callout .phone { font-size: 44px; margin-top: 4px; letter-spacing: 0.5px; }
  .headline {
    position: absolute;
    left: 90px;
    top: 446px;
    margin: 0;
    font-size: 36px;
    font-weight: 800;
    line-height: 50px;
    text-transform: uppercase;
    letter-spacing: 0.3px;
  }
  .info-panel {
    position: absolute;
    left: 26px;
    top: 681px;
    width: 887px;
    height: 489px;
    background: var(--teal);
  }
  .brand {
    position: absolute;
    left: 88px;
    top: 250px;
    display: flex;
    align-items: center;
    gap: 14px;
    font-size: 30px;
    font-weight: 800;
    color: var(--navy);
    line-height: 1.05;
  }
  .brand-dot {
    width: 44px;
    height: 44px;
    border-radius: 50%;
    background: var(--navy);
    flex: none;
  }
  .services-copy {
    position: absolute;
    left: 438px;
    top: 32px;
    width: 386px;
    margin: 0;
    font-size: 14.6px;
    font-weight: 700;
    line-height: 16.8px;
    text-align: justify;
  }
  .services-copy p { margin: 0; }
</style>
</head>
<body>
<div class="flyer">
  <section class="hero" role="img" aria-label="Photograph of floodwater reaching a brick doorway with a pump hose draining the water">
    <div class="hero-water"></div>
  </section>

  <div class="service-callout">
    <div class="hours">24/7</div>
    <div class="label">Service</div>
    <div class="call">Please call</div>
    <div class="phone">+1 000 000</div>
  </div>

  <h1 class="headline">Solution for<br>water restoration<br>and<br>flood damage</h1>

  <section class="info-panel">
    <div class="brand">
      <span class="brand-dot"></span>
      <span>Brindlewick<br>Building Group</span>
    </div>
    <div class="services-copy">
      <p>We provide disaster relief to homeowners and or commercial property owners after a flood.</p>
      <p>To start we offer cleanup and remediation which is taking out and disposing of all wet items in a home or business and the cutting out of walls, flooring and other items affected by a flood.</p>
      <p>We then provide remediation which includes the drying out of a home or business along with a dehumidifier to take all the moisture out of the air and to put it simply dry out the home.</p>
      <p>We also uses chemicals to clean and provide mold remediation to prevent to growth of mold.</p>
      <p>We work directly with a customers insurance company if they have flood insurance and after that we provide the services to rebuild and bring their property back to its condition before the storm.</p>
    </div>
  </section>
</div>
</body>
</html>
```